Goodlooking website for a company who is working in the IT consultancy

We want a new website designed in WordPress. You can take www.vantorq.nl as an example. It should be a website with some short blocks of information about the company, nice pictures of our partners and our employees. A job page with a clear filter.

Target Market(s)

B2B

Industry/Entity Type

It Company

Coding

Coded - Design and coding required

Number of Pages Required

5+ page

Font styles to use
Sans Serif

Colors
0455a3
34a7d8

Requirements
Must have
• Check briefing

```html
<!DOCTYPE html>
<html lang="en">
<head>
<meta charset="utf-8">
<title>Contact Us – Vantorq</title>
<link href="https://fonts.googleapis.com/css2?family=PT+Sans:wght@400;700&display=swap" rel="stylesheet">
<style>
  :root {
    --brand-teal: #34a7d8;
    --nav-active: #4fb3c8;
    --banner-deep: #1f7fa3;
    --banner-light: #5fb0cc;
    --accent-green: #14a08f;
    --ink: #2b2b2b;
    --muted: #777777;
    --line: #d8d8d8;
    --page-bg: #f7f7f7;
    --crumb-bg: #f0f0f0;
    --map-base: #dde3e1;
    --map-soft: #cfdcdd;
    --footer-bg: #2f2f2f;
    --footer-bottom: #3a3a3a;
    --footer-text: #c9c9c9;
    --footer-dim: #8e8e8e;
    --footer-rule: #4a4a4a;
    --white: #ffffff;
  }
  * { box-sizing: border-box; margin: 0; padding: 0; }
  html, body { width: 1200px; height: 1200px; overflow: hidden; }
  body {
    position: relative;
    font-family: "PT Sans", Arial, sans-serif;
    background: var(--page-bg);
    color: var(--ink);
  }
  .abs { position: absolute; }

  /* Header */
  .site-header { left: 0; top: 0; width: 1200px; height: 72px; background: var(--white); box-shadow: 0 1px 3px rgba(0,0,0,.08); z-index: 2; }
  .brand { left: 170px; top: 8px; display: flex; align-items: center; gap: 10px; }
  .brand-dot { width: 52px; height: 52px; border-radius: 50%; background: var(--brand-teal); }
  .brand-text { display: flex; flex-direction: column; }
  .brand-name { font-size: 32px; font-weight: 400; letter-spacing: 3px; color: #3a4a55; line-height: 1; }
  .brand-tag { font-size: 7px; letter-spacing: 1.5px; color: var(--brand-teal); margin-top: 3px; padding-left: 16px; }
  .main-nav a { position: absolute; top: 0; height: 72px; line-height: 70px; font-size: 10px; font-weight: 700; color: #777; text-decoration: none; letter-spacing: .2px; }
  .main-nav .active { background: var(--nav-active); color: var(--white); width: 80px; text-align: center; }

  /* Banner */
  .page-banner { left: 0; top: 72px; width: 1200px; height: 98px; background: linear-gradient(90deg, var(--banner-deep) 0%, #3b95b8 55%, var(--banner-light) 100%); }
  .page-title { left: 170px; top: 106px; font-size: 24px; font-weight: 700; color: var(--white); }

  .breadcrumb { left: 0; top: 170px; width: 1200px; height: 40px; background: var(--crumb-bg); border-bottom: 1px solid #e2e2e2; }
  .breadcrumb span { position: absolute; left: 170px; top: 13px; font-size: 11px; font-weight: 700; letter-spacing: .5px; color: #333; }

  /* Content */
  .section-title { font-size: 18px; font-weight: 700; color: #333; }
  .rule { height: 1px; background: var(--line); }
  .office-map { left: 170px; top: 313px; width: 495px; height: 377px; background: linear-gradient(160deg, var(--map-base) 0%, var(--map-soft) 100%); }

  .field-label { font-size: 12px; font-weight: 700; color: #333; }
  .field { left: 721px; width: 285px; background: var(--white); border: 1px solid #cfcfcf; font-size: 11px; color: #777; padding: 12px 10px; }
  .submit-btn { left: 721px; top: 702px; width: 98px; height: 30px; border-radius: 15px; background: var(--accent-green); color: var(--white); font-size: 11px; font-weight: 700; letter-spacing: .8px; display: flex; align-items: center; justify-content: center; gap: 8px; box-shadow: 0 2px 0 #0c7a6d; }

  /* Footer */
  .site-footer { left: 0; top: 777px; width: 1200px; height: 337px; background: var(--footer-bg); }
  .footer-heading { top: 828px; font-size: 15px; font-weight: 400; letter-spacing: 1px; color: var(--white); }
  .footer-rule { top: 855px; height: 1px; background: var(--footer-rule); }
  .footer-rule::before { content: ""; position: absolute; left: 0; top: 0; width: 35px; height: 2px; background: var(--brand-teal); }
  .info-label { font-size: 12px; letter-spacing: 1px; color: var(--white); }
  .info-text { font-size: 12px; letter-spacing: 1px; color: var(--footer-text); line-height: 18px; }
  .link-list { list-style: none; }
  .link-list li { height: 32px; border-bottom: 1px solid #3e3e3e; font-size: 12px; letter-spacing: 1.2px; color: var(--footer-text); padding-top: 8px; width: 132px; }
  .link-list li::before { content: "»"; color: var(--footer-dim); margin-right: 14px; }
  .link-list li:last-child { border-bottom: none; }
  .footer-bottom { left: 0; top: 1114px; width: 1200px; height: 86px; background: var(--footer-bottom); }
  .social { top: 1131px; width: 34px; height: 34px; border: 1px solid #555; border-radius: 50%; }
  .copyright { left: 0; top: 1174px; width: 1200px; text-align: center; font-size: 11px; letter-spacing: 1px; color: var(--footer-dim); }
</style>
</head>
<body>

<header class="abs site-header">
  <div class="abs brand">
    <div class="brand-dot"></div>
    <div class="brand-text">
      <span class="brand-name">VANTORQ</span>
      <span class="brand-tag">CRITICAL IT SYSTEMS</span>
    </div>
  </div>
  <nav class="main-nav">
    <a style="left:644px">HOME</a>
    <a style="left:710px">OUR SOLUTIONS</a>
    <a style="left:823px">OUR TEAM</a>
    <a style="left:910px">JOBS</a>
    <a class="active" style="left:950px">CONTACT</a>
  </nav>
</header>

<div class="abs page-banner" role="img" aria-label="Photo of glass office towers in blue tones"></div>
<h1 class="abs page-title">Contact Us</h1>

<div class="abs breadcrumb"><span>Home &gt; Contact Us</span></div>

<h2 class="abs section-title" style="left:170px;top:260px">Office Location</h2>
<div class="abs rule" style="left:170px;top:295px;width:495px"></div>
<div class="abs office-map" role="img" aria-label="Street map showing the office location"></div>

<h2 class="abs section-title" style="left:721px;top:260px">Start a Conversation</h2>
<div class="abs rule" style="left:721px;top:295px;width:285px"></div>

<label class="abs field-label" style="left:721px;top:314px">Name</label>
<div class="abs field" style="top:334px;height:36px">Your Full Name</div>
<label class="abs field-label" style="left:721px;top:387px">Email</label>
<div class="abs field" style="top:407px;height:36px">Valid Email Address</div>
<label class="abs field-label" style="left:721px;top:459px">Phone</label>
<div class="abs field" style="top:480px;height:36px">Your Contact Number</div>
<label class="abs field-label" style="left:721px;top:532px">Message</label>
<div class="abs field" style="top:552px;height:134px">Your Message</div>

<div class="abs submit-btn">SUBMIT
  <svg width="12" height="12" viewBox="0 0 24 24"><path d="M2 11 22 2 15 22 11 13Z" fill="#fff"/></svg>
</div>

<footer class="abs site-footer"></footer>

<h3 class="abs footer-heading" style="left:191px">Contact Info</h3>
<div class="abs footer-rule" style="left:191px;width:181px"></div>
<h3 class="abs footer-heading" style="left:417px">Quick Links</h3>
<div class="abs footer-rule" style="left:417px;width:132px"></div>
<h3 class="abs footer-heading" style="left:594px">Support</h3>
<div class="abs footer-rule" style="left:594px;width:141px"></div>
<h3 class="abs footer-heading" style="left:780px">Join Our Newsletter</h3>
<div class="abs footer-rule" style="left:780px;width:228px"></div>

<svg class="abs" style="left:194px;top:884px" width="12" height="16" viewBox="0 0 12 16"><path d="M6 0a6 6 0 0 0-6 6c0 4.5 6 10 6 10s6-5.5 6-10a6 6 0 0 0-6-6Zm0 8.5a2.5 2.5 0 1 1 0-5 2.5 2.5 0 0 1 0 5Z" fill="#34a7d8"/></svg>
<div class="abs info-label" style="left:218px;top:883px">Address:</div>
<div class="abs info-text" style="left:218px;top:904px">Melodielaan 14,<br>3421 KT Veldhoven</div>

<svg class="abs" style="left:193px;top:958px" width="14" height="14" viewBox="0 0 24 24"><path d="M6.6 10.8a15 15 0 0 0 6.6 6.6l2.2-2.2c.3-.3.7-.4 1-.2 1.1.4 2.3.6 3.6.6.6 0 1 .4 1 1V20c0 .6-.4 1-1 1A17 17 0 0 1 3 4c0-.6.4-1 1-1h3.5c.6 0 1 .4 1 1 0 1.3.2 2.5.6 3.6.1.3 0 .7-.2 1Z" fill="#34a7d8"/></svg>
<div class="abs info-label" style="left:218px;top:958px">Phone:</div>
<div class="abs info-text" style="left:218px;top:980px;font-size:15px">085-3716042</div>

<svg class="abs" style="left:192px;top:1024px" width="15" height="11" viewBox="0 0 15 11"><rect width="15" height="11" fill="#34a7d8"/><path d="M0 0 7.5 6 15 0" stroke="#2f2f2f" fill="none"/></svg>
<div class="abs info-label" style="left:217px;top:1020px">Email:</div>
<div class="abs info-text" style="left:217px;top:1042px;font-size:15px;color:#34a7d8">info@vantorq.nl</div>

<ul class="abs link-list" style="left:419px;top:880px">
  <li>Home</li><li>Our Solutions</li><li>Our Team</li><li>Jobs</li><li>Contact</li>
</ul>
<ul class="abs link-list" style="left:596px;top:880px">
  <li>Terms of Use</li><li>Privacy Policy</li><li>Cookie Policy</li>
</ul>

<div class="abs info-text" style="left:780px;top:884px;color:#8e8e8e;letter-spacing:0">Subscribe for Job Alerts and Updates!</div>
<div class="abs" style="left:780px;top:917px;width:228px;height:30px;background:#fff;font-size:11px;color:#888;padding:8px 11px">Enter Your Email</div>
<div class="abs" style="left:780px;top:956px;width:102px;height:30px;border-radius:15px;background:#4a4a4a;color:#fff;font-size:12px;display:flex;align-items:center;justify-content:center;gap:8px">
  <svg width="12" height="12" viewBox="0 0 24 24"><path d="M2 11 22 2 15 22 11 13Z" fill="#fff"/></svg>Subscribe
</div>

<div class="abs footer-bottom"></div>
<div class="abs social" style="left:565px"></div>
<div class="abs social" style="left:601px"></div>
<div class="abs copyright">Copyright © 2018 VANTORQ. All Rights Reserved.</div>

</body>
</html>
```